Chart Your Own Harbor Promotional Flyer

I Need a one page, one-sided 8.5 x 11 editable promotional flyer that POPS!, designed in photoshop

[TITLE]Chart Your Own Harbor: 3 BRIGHT Steps to Lift Your Practice Today!

[CONTENT for the Flyer:]

At this content-rich event you will learn how to:
• Get out of feast and famine mode and into six, multi-six and/or seven figure-income mode
• Leapfrog your competition and become the obvious choice in your market
• Have your business aligned with who you are and what you want
• Enjoy your business far more than you imagined possible.
• Have more fun and time to yourself
• Live free and unbound!

Accolades
“Delphine helped us increase our six figure income by 41%...I feel reborn!” Marlene & Otis Pruitt, Vienna, VA

“…Delphine is a joy to listen to - compelling, smart, provocative…” – Dwight Fennimore, Charlotte, North Carolina

“Delphine helped me increase my business by 66%...without me spending more time, money, or making cold calls! …I am in the zone!” Tess Calloway, Baltimore, MD
“Delphine is an energetic and dynamic speaker…content-rich…holds your attention to the very end!” Hal Brisbee, Frmr Pres., Kemper & Vail, MD, MD, D.C., PA, DE, NJ
“Delphine is the real estate whisperer!” Lou Tremaine, Washington D.C.

“Delphine was prepared, funny, informative and made a connection with each of our agents…Fabulous!…even my admins were PUMPED!!! – Paul Devereux, New York

About Delphine:
Delphine is a highly regarded business development speaker & coach who knows how to pump up an audience and have them making more money, in less time, AND having more fun doing it! What’s not to love?! Consistently rated as an exceptional speaker and conference favorite! Among her work: Magnet Method: How to Draw Your Dream Buyers Time After Time!, Client Pipelines Without Fuss, The Costliest Outreach Blunders Real Estate Agents Commit and How to Sidestep Them, Hard Seasons Forge Hard Sellers, Fuel for the Spirit for Real Estate Agents.

[Also need a section for:]
Date: December 9, 2015, Time: 9:00 Am - 12:00 Noon, Place: Silver Maple Conference, Ashford Hollow, PA

Target Market(s)

Real Estate Agents

Industry/Entity Type

Real Estate Agent

Font styles to use
Sans Serif

Colors
0655a3
f37122

Requirements
Must have
• the top tier prop mentor logo
Nice to have
• chart your own harbor logo; lots of POP! :-) ; open to other colors, accent colors.

```html
<!DOCTYPE html>
<html lang="en">
<head>
<meta charset="utf-8">
<title>Chart Your Own Harbor – Event Flyer</title>
<link href="https://fonts.googleapis.com/css2?family=Titan+One&family=Archivo+Black&family=Open+Sans:ital,wght@0,400;0,700;0,800;1,700;1,800&display=swap" rel="stylesheet">
<style>
  :root {
    --brand-blue: #0655a3;
    --brand-orange: #f37122;
    --orange-light: #ffb15a;
    --orange-deep: #e8621a;
    --sky-top: #7fb6ec;
    --sky-bottom: #1d62c8;
    --ink: #1c1c1c;
    --paper: #ffffff;
  }
  * { margin: 0; padding: 0; box-sizing: border-box; }
  html, body { width: 927px; height: 1200px; overflow: hidden; background: var(--paper); }
  .flyer { position: relative; width: 927px; height: 1200px; overflow: hidden; background: var(--paper); font-family: "Open Sans", Arial, sans-serif; color: var(--ink); }

  .headline {
    position: absolute; left: 0; right: 0; top: 8px; text-align: center;
    font-family: "Titan One", "Arial Black", sans-serif;
    font-size: 74px; line-height: 82px; letter-spacing: 5px;
    background: linear-gradient(180deg, var(--orange-light) 10%, var(--brand-orange) 55%, var(--orange-deep) 100%);
    -webkit-background-clip: text; background-clip: text; color: transparent;
    filter: drop-shadow(2px 3px 2px rgba(0,0,0,.35));
  }
  .subhead {
    position: absolute; left: 0; right: 0; top: 190px; text-align: center;
    font-family: "Archivo Black", "Arial Black", sans-serif;
    font-size: 27px; letter-spacing: 2px; color: var(--brand-blue);
    text-shadow: 1px 2px 2px rgba(0,0,0,.3);
  }

  .learn-box {
    position: absolute; left: 117px; top: 253px; width: 694px; height: 344px;
    background: linear-gradient(180deg, var(--sky-top) 0%, #4d8fdc 35%, var(--sky-bottom) 100%);
    box-shadow: 0 2px 4px rgba(0,0,0,.35); color: var(--paper);
    font-weight: 700;
  }
  .learn-box h2 { font-size: 22.5px; font-weight: 700; letter-spacing: .6px; margin: 22px 0 0 14px; text-shadow: 1px 1px 2px rgba(0,0,0,.3); }
  .learn-box ul { list-style: none; margin: 8px 0 0 103px; width: 510px; font-size: 19px; line-height: 29.6px; letter-spacing: .2px; }

  .event-details {
    position: absolute; left: 117px; top: 603px; width: 694px; height: 107px;
    border: 3px solid var(--orange-deep); text-align: center;
    font-size: 21.5px; line-height: 26.5px; padding-top: 12px; letter-spacing: .4px;
  }
  .event-details b { font-weight: 800; font-style: italic; }

  .accolades { position: absolute; left: 18px; top: 738px; width: 445px; font-size: 14.5px; line-height: 18px; }
  .accolades p { margin-bottom: 24px; }
  .accolades q { font-weight: 800; font-style: italic; quotes: "\201C" "\201D"; font-size: 15.5px; }
  .accolades cite { font-style: italic; }

  .about { position: absolute; left: 497px; top: 738px; width: 422px; font-size: 14.4px; line-height: 17.4px; font-weight: 700; }
  .about h3 { font-size: 16px; font-weight: 700; margin-bottom: 1px; }

  .harbor-mark { position: absolute; left: 36px; top: 1062px; display: flex; align-items: center; gap: 12px; color: var(--brand-blue); font-size: 34px; font-weight: 700; }
  .harbor-mark .dot { width: 30px; height: 30px; border-radius: 50%; background: var(--brand-orange); }

  .mentor-name { position: absolute; left: 518px; top: 1018px; width: 220px; text-align: center; color: #8a8a8a; font-weight: 700; font-size: 24px; line-height: 30px; }
  .mentor-mark { position: absolute; left: 518px; top: 1052px; width: 220px; text-align: center; color: var(--brand-orange); font-weight: 800; font-size: 27px; line-height: 30px; }

  .portrait { position: absolute; left: 745px; top: 1005px; width: 182px; height: 170px; background: linear-gradient(180deg, #e9e9e9 0%, #c9a978 45%, #2a2a2a 100%); }

  .footer-band { position: absolute; left: 0; bottom: 0; width: 927px; height: 25px; background: var(--orange-deep); color: var(--paper); text-align: right; padding-right: 30px; font-size: 14px; font-style: italic; line-height: 25px; }
</style>
</head>
<body>
<main class="flyer">
  <h1 class="headline">CHART YOUR OWN<br>HARBOR</h1>
  <p class="subhead">3 BRIGHT STEPS TO LIFT YOUR PRACTICE TODAY !</p>

  <section class="learn-box">
    <h2>At this content-rich event you will learn how to:</h2>
    <ul>
      <li>• Get out of feast and famine mode and into six, multi-six and/or seven figure-income mode</li>
      <li>• Leapfrog your competition and become the obvious choice in your market</li>
      <li>• Have your business aligned with who you are and what you want</li>
      <li>• Enjoy your business far more than you imagined possible.</li>
      <li>• Have more fun and time to yourself</li>
    </ul>
  </section>

  <section class="event-details">
    Date: <b>December 9, 2015</b><br>
    Time: <b>9:00 Am - 12:00 Noon</b><br>
    Place: <b>Silver Maple Conference, Ashford Hollow, PA</b>
  </section>

  <section class="accolades">
    <p><q>Delphine helped us increase our six figure income by 41%...I feel reborn!</q> <cite>Marlene &amp; Otis Pruitt, Vienna, VA</cite></p>
    <p><q>…Delphine is a joy to listen to - compelling, smart, provocative…</q> <cite>Dwight Fennimore, Charlotte, North Carolina</cite></p>
    <p><q>Delphine helped me increase my business by 66%...without me spending more time, money, or making cold calls! …I am in the zone!</q> <cite>Tess Calloway, Baltimore, MD</cite></p>
    <p><q>Delphine is the real estate whisperer!</q> <cite>Lou Tremaine, Washington D.C.</cite></p>
  </section>

  <section class="about">
    <h3>About Delphine:</h3>
    <p>Delphine is a highly regarded business development speaker &amp; coach who knows how to pump up an audience and have them making more money, in less time, AND having more fun doing it! What’s not to love?! Consistently rated as an exceptional speaker and conference favorite!<br>
    Among her work: Magnet Method: How to Draw Your Dream Buyers Time After Time!, Client Pipelines Without Fuss, The Costliest Outreach Blunders Real Estate Agents Commit and How to Sidestep Them, Hard Seasons Forge Hard Sellers, Fuel for the Spirit for Real Estate Agents.</p>
  </section>

  <div class="harbor-mark"><span class="dot"></span><span>Chart Your Own Harbor</span></div>

  <div class="mentor-name">Delphine Marsh</div>
  <div class="mentor-mark">Top Tier Prop Mentor</div>

  <div class="portrait" role="img" aria-label="Portrait photo of Delphine Marsh, smiling, in a dark blazer"></div>

  <footer class="footer-band">“America’s Top Tier Prop Mentor”™</footer>
</main>
</body>
</html>
```